Website for the recruitment firm vorl

Objective :

Create a modern, elegant, and understated website with a touch of sophistication. The site must be fully custom-coded (or custom-coded on WordPress), responsive, and fast, reflecting the quality and high standards of our firm.

It must be bilingual (FR/EN), with a language selector visible in the header.

About vorl.

vorl. is a high-end recruitment firm, led by experienced consultants—employees and freelancers—and supported by a dedicated team of recruitment managers. Our hybrid approach allows us to handle complex, confidential, or high-volume projects with rigor and agility.

We operate across several business verticals:

Executive

Finance & Advisory (accounting, management control, treasury, corporate finance, financial consulting or investment banking)

Legal

Audit & Expertise

People & Office

Supply & Purchasing

Industry & Engineering

Our approach is based on a balance between human know-how and cutting-edge technologies (AI, automation, data) to respond to recruitment challenges with accuracy, responsiveness and impact.

Slogan: Expertise at the service of every recruitment.

Purpose of the site:

Client side: present our expertise, our values, our support.

Candidate side: allow the search for offers, by expertise.

On the consultant side: encouraging freelancers or employees to join us.

Structure & pages requested:

Welcome

Main banner with slogan and strong visual (possibility of a background video like maltevo.ca — for a modern and dynamic look)

Clear redirection to both paths: “I’m looking for talent” / “I want to join vorl. ”

Quick presentation of expertise with redirection to each dedicated page

Highlighting values

About

Our mission

Our values (excellence, flexibility, partnership)

Our hybrid operation (in-house and independent consultants)

The recruitment team and the support offered

Expertise (1 page per vertical, with color code specific to each division)

Description of the professions recruited

Key skills

Typical customer profiles

Testimonials or case studies (placeholder)

Button/CTA to offers corresponding to this expertise

Job offers

Page with filter by expertise

“Join vorl” option with our internal offers (consultants, recruitment managers, etc.)

Join us

Why work with vorl.

Independent vs. employee path

Tools provided, support, internal training

Highlighting the support team and recruitment managers

Contact

Form

Email + LinkedIn link

Design requirements:

Font: Gazette LT Std or contemporary serif with a strong identity

Color code by division (the background or page elements must match the color of the expertise):

vorl. / vorl.group. → #000000 (black)

vorl.executive. → #2F4F4F (dark green)

vorl.finance&advisory. → #0B1E36 (midnight blue)

vorl.people&office. → #f2b8b8 (powder pink)

vorl.audit&expertise. → #993294 (plum)

vorl.legal. → #d9a00f (yellow gold)

vorl.supply&purchasing. → #CE8946 (rust bronze)

vorl.industry&engineering. → #9e9b9e (light silver gray)

Technical features:

100% responsive and mobile-friendly design

Fast charging

Own structure (SEO-friendly)

Simple back-office interface for updating offers

Language selector FR / EN

Inspirations to consult:

For the tree structure, tabs and ergonomics: tindle-bray.com

For visual ambiance / video / animation: maltevo.ca

Expected deliverables:

Full site (online or compressed file)

All source files (HTML/CSS/JS or custom Wordpress)

Favicon

Brand guideline (PDF) with:

Typographies used

HEX color codes

Margins and line spacing

Examples of use of light and dark background logo

Optional: template for email signature

Objective
Design a modern, elegant and clean website with a touch of sophistication. The site must be fully custom-coded (or built with custom WordPress development), responsive, fast, and reflect the premium standards and quality of our recruitment firm.

It must be bilingual (FR/EN), with a clearly visible language selector in the header.

About vorl.
vorl. is a premium recruitment firm driven by experienced consultants — whether in-house or freelance — supported by a dedicated team of recruitment coordinators. Our hybrid model allows us to handle complex, confidential, or high-volume recruitment assignments with both precision and agility.

We operate across several verticals:

Executive

Finance & Advisory (accounting, controlling, treasury, corporate finance, investment banking advisory)

Legal

Audit & Expertise

People & Office

Supply & Purchasing

Industry & Engineering

Our approach combines human expertise with cutting-edge technologies (AI, automation, data) to tackle recruitment challenges with accuracy, speed, and impact.

Tagline: Expertise serving every recruitment need.

Website Purpose
Client-facing: highlight our expertise, values, and recruitment support model.

Candidate-facing: allow job seekers to explore openings by area of expertise.

Consultant-facing: attract freelance or in-house recruiters to join vorl.

Site Structure & Required Pages
Home
Hero banner with tagline and impactful visual (option for background video, eg maltevo. That)

Clear user path: “I'm looking to hire” / “I want to join vorl. ”

Quick intro to our expertise areas with links to each division page

Highlight our values and unique model

About Us
Our mission

Our hybrid recruitment model (internal consultants + freelancers)

Our recruitment support team and how we work

Expertise (1 page per vertical, using the division's brand color)
Each division page should include:

Description of roles we recruit

Key skills

Typical client profiles

Placeholder for testimonials or success stories

CTA linking to job openings relevant to the division

Verticals:

Executive

Finance & Advisory

Legal

Audit & Expertise

People & Office

Supply & Purchasing

Industry & Engineering

Job Offers
Central job board with filter by expertise

Section: “Join vorl. ” with internal positions (consultants, recruitment coordinators, etc.)

Join Us
Why join vorl.

Independent vs. permanent contract path

Tools, training and operational support

Highlight the internal sourcing and recruitment support team

Contact
Contact form

Email + LinkedIn link

Design Requirements
Font: Gazette LT Std or similar contemporary serif with strong identity

Each vertical should have its own dedicated brand color applied to its page background or key elements:

Division HEX Code Color Description
vorl. /vorl.group. #000000 Black
vorl.executive #2F4F4F Dark green
vorl.finance&advisory #0B1E36 Navy blue
vorl.people&office #f2b8b8 Powder pink
vorl.audit&expertise #993294 Plum
vorl.legal #d9a00f Golden yellow
vorl.supply&purchasing #CE8946 Rust bronze
vorl. industry&engineering #9e9b9e Light silver gray

Technical Features
Fully responsive and mobile-friendly

Fast loading

Clean structure, SEO optimized

Simple back-office interface for job posting and updates

Bilingual switch: FR / EN

Inspirations
For navigation, structure, and user interface:
🔗 https://www.tindle-bray.com/fr/fr/

For visual style, animations, and dynamic video intro:
🔗 https://maltevo.ca/

Deliverables
Fully functional website (live or delivered as a complete package)

All source files (HTML/CSS/JS or custom WordPress)

Favicon

Brand guideline (PDF) including:

Fonts used

HEX color codes

Spacing and layout guidelines

Logo usage on dark/light backgrounds

Optional: email signature template

Target Market(s)

Recruitment firm environment

Industry/Entity Type

Hi, A few clarifications to guide the website structure. The site should be clearly built around three main sections, each addressing a specific target audience: 1. For Clients – “Looking to hire?” This section will highlight our recruitment services, industry expertise, and tailored approach. 2. For Candidates – “Looking for a job?” A space where candidates can explore job offers by sector and apply directly. 3. For Experts – “Want to join us?” This area is for recruitment professionals (consultants or talent acquisition specialists) interested in joining vorl., either as employees or as independents. It should showcase the tools, support, and working environment we offer. These three user paths should be clearly visible on the homepage, using clear buttons or dedicated sections to ensure smooth navigation.

Coding

Coded - Design and coding required

Number of Pages Required

5+ page

Font styles to use
Other font styles liked:
• Gazette LT Std

Colors

Designer to choose colors to be used in the design.

Requirements
Must have
• Essentials – Section Ideas Our hybrid model → Clear presentation of employee/freelance cohabitation, and how it brings flexibility and efficiency to clients. Our quality commitment → Rigorous methodology, transparency, customer satisfaction, tailor-made support. Our augmented approach → Highlighting the use of AI tools, intelligent CRM, automated multi-channel sourcing, predictive tests, etc. Our support team → Promotion of the team of recruitment managers who support the consultants, guaranteeing responsiveness and depth in the hunt. Our areas of expertise → Mini-grid or mosaic that links to the main verticals (useful for cross-functional reinforcement).
Nice to have
• CRM / ATS Integration Direct connection with our application management tool (Velump type or other), for seamless synchronization of offers, applications and follow-ups. 📱 Progressive web app version (PWA) A site accessible in mobile application mode, for a smooth, fast and accessible offline user experience.

```html
<!DOCTYPE html>
<html lang="en">
<head>
<meta charset="utf-8">
<title>vorl. — Expertise serving every recruitment need</title>
<link rel="stylesheet" href="https://fonts.googleapis.com/css2?family=DM+Serif+Display&family=Mulish:wght@300;400;500;600&display=swap">
<style>
:root{
  --black:#000000;
  --white:#ffffff;
  --orange:#f26a1b;
  --cream:#f3efe0;
  --executive:#2F4F4F;
  --finance:#0B1E36;
  --legal:#d9a00f;
  --audit:#8e2392;
  --people:#eba9a9;
  --supply:#c47a38;
  --industry:#8f8c8f;
  --ink:#1b1b1b;
  --muted:#555555;
  --serif:'DM Serif Display', Georgia, serif;
  --sans:'Mulish', Arial, sans-serif;
}
*{box-sizing:border-box;margin:0;padding:0}
html,body{width:1200px;height:4691px;overflow:hidden}
body{position:relative;background:var(--white);font-family:var(--sans);color:var(--ink)}
.abs{position:absolute}
a{color:inherit;text-decoration:none}
.arrow{display:inline-block;width:24px;height:10px;vertical-align:middle;margin-left:12px}

/* hero */
.hero{left:0;top:0;width:1200px;height:1500px;background:var(--black)}
.hero-photo{left:0;top:0;width:1200px;height:700px;
  background:linear-gradient(180deg,rgba(0,0,0,0) 55%,#000 100%),
  radial-gradient(ellipse at 78% 40%,#7b6a5c 0%,#4a4540 35%,#2a2a2a 70%),#222}
.nav{left:0;top:0;width:1200px;height:100px}
.logo{font-family:var(--serif);color:var(--white);font-size:58px;line-height:1}
.nav .logo{left:149px;top:20px}
.nav-item{font-family:var(--serif);color:var(--white);font-size:14px;top:39px}
.nav-home{left:344px;top:31px;width:68px;height:36px;border:1.5px solid var(--white);border-radius:18px;text-align:center;line-height:33px;font-family:var(--serif);color:var(--white);font-size:14px}
.nav-sep{left:823px;top:30px;width:1px;height:38px;background:var(--white)}
.btn{background:var(--orange);color:var(--white);font-family:var(--serif);border-radius:12px;text-align:center}
.join{left:907px;top:29px;width:142px;height:40px;line-height:40px;font-size:14px;border-radius:14px}
.hero h1{left:149px;top:162px;width:560px;font-family:var(--serif);font-weight:400;color:var(--white);font-size:56px;line-height:64px}
.cta{left:149px;width:241px;height:52px;line-height:52px;font-size:17px;font-family:var(--serif);border-radius:12px;text-align:center}
.cta-hire{top:404px;background:var(--orange);color:var(--white)}
.cta-join{top:478px;background:var(--cream);color:var(--ink)}
.play{left:552px;top:524px;width:133px;height:34px;border-radius:17px;background:rgba(0,0,0,.75);color:var(--white);font-family:var(--serif);font-size:12px;line-height:34px;padding-left:40px}
.play svg{position:absolute;left:8px;top:6px}

/* welcome */
.welcome{left:118px;top:779px;width:971px;height:289px;border:1px solid #777;border-radius:22px}
.welcome h2{left:0;top:-30px;width:100%;text-align:center}
.welcome h2 span{background:var(--black);padding:0 22px;font-family:var(--serif);font-weight:400;color:var(--white);font-size:52px}
.rule{height:2px;background:currentColor}
.welcome .rule{left:456px;top:62px;width:52px;color:var(--white)}
.welcome p{left:120px;top:106px;width:731px;text-align:center;color:#e5e5e5;font-size:17px;line-height:29px;font-weight:300}
.read-more{left:401px;top:263px;width:168px;height:47px;line-height:47px;font-size:17px}
.strip{top:1175px;width:275px;height:247px;border-radius:8px}

/* sectors */
.sectors{left:0;top:1499px;width:1200px;height:1060px;background:var(--white);border-radius:80px 80px 0 0}
.section-title{font-family:var(--serif);font-weight:400;font-size:44px;color:var(--ink)}
.sectors .section-title{left:0;top:42px;width:1200px;text-align:center}
.sectors .rule{left:574px;top:109px;width:52px;color:var(--ink)}
.card{border-radius:6px;color:var(--white)}
.card .brand{left:26px;top:22px;font-family:var(--serif);font-size:34px;line-height:1}
.card .brand small{position:absolute;left:14px;top:36px;font-family:var(--sans);font-size:7px;white-space:nowrap;letter-spacing:.3px;opacity:.85}
.card .icon{width:84px;height:84px;border:1.5px solid var(--white);border-radius:50%;top:82px}
.card .icon svg{position:absolute;left:22px;top:22px}
.card h3{left:22px;top:192px;font-family:var(--serif);font-weight:400;font-size:17px}
.card p{left:22px;top:228px;font-size:11.5px;line-height:15px}
.card .more{left:22px;top:334px;height:27px;line-height:24px;padding:0 12px;border:1.5px solid var(--white);border-radius:14px;font-family:var(--serif);font-size:10px}

/* values */
.values{left:0;top:2546px;width:1200px;height:660px;
  background:repeating-linear-gradient(135deg,#f3f3f3 0 140px,#e9e9e9 140px 300px)}
.values .section-title{left:149px;top:36px}
.values .rule{left:149px;top:103px;width:52px;color:var(--ink)}
.value-icon{left:146px;width:90px;height:90px;border-radius:50%;background:var(--orange)}
.value-icon svg{position:absolute;left:25px;top:25px}
.value h3{left:261px;font-family:var(--serif);font-weight:400;font-size:22px}
.value p{left:261px;width:320px;font-size:12px;line-height:17px;color:var(--muted)}
.value-rule{left:149px;width:445px;height:1px;background:#555}
.circle-photo{border-radius:50%}

/* commitments */
.approach{left:0;top:3150px;width:1200px;height:680px;background:var(--black);border-radius:70px 70px 0 0}
.approach-photo{top:64px;width:434px;height:342px;border-radius:8px}
.approach h3{font-family:var(--serif);font-weight:400;color:var(--white);font-size:28px;line-height:33px}
.approach-rule{height:1px;background:#444}
.points{list-style:none;color:var(--white);font-size:12.5px;line-height:15px}
.points li{position:relative;padding:6px 0 6px 14px;border-bottom:1px solid #3a3a3a}
.points li::before{content:"";position:absolute;left:2px;top:10px;border-left:5px solid var(--white);border-top:4px solid transparent;border-bottom:4px solid transparent}

/* hybrid */
.hybrid-photo{left:149px;top:3861px;width:528px;height:406px;border-radius:10px}
.hybrid h2{left:741px;top:3916px;font-family:var(--serif);font-weight:400;font-size:46px;line-height:52px;color:var(--ink)}
.hybrid .rule{left:743px;top:4046px;width:52px;color:var(--ink)}
.hybrid p{left:743px;top:4084px;width:300px;font-size:17.5px;line-height:27px;color:var(--ink)}

/* footer */
.footer{left:0;top:4325px;width:1200px;height:366px;background:var(--cream);border-radius:70px 70px 0 0}
.footer .logo{left:149px;top:90px;color:var(--black);font-size:120px}
.footer h4{font-family:var(--serif);font-weight:400;font-size:16px;color:var(--ink)}
.menu{left:462px;top:95px;list-style:none;font-size:12px;line-height:22.5px}
.field{left:601px;width:182px;height:31px;border:1px solid #aaa;border-radius:8px;background:var(--white);font-size:10px;padding:8px 12px;color:#444}
.message{left:794px;top:89px;width:255px;height:115px;border:1px solid #aaa;border-radius:8px;background:var(--white);font-size:10px;padding:8px 12px;color:#444}
.follow{left:147px;top:237px;font-family:var(--serif);font-size:16px}
.social{top:234px;width:32px;height:32px;border-radius:50%}
.foot-line{left:459px;top:249px;width:470px;height:1.5px;background:#333}
.submit{left:956px;top:231px;width:95px;height:37px;line-height:37px;font-size:16px;border-radius:6px}
.copyright{left:0;top:307px;width:1200px;text-align:center;font-size:11px;color:#333}
</style>
</head>
<body>

<section class="hero abs">
  <div class="hero-photo abs" role="img" aria-label="Photo of two professionals smiling and talking in a bright office"></div>
  <header class="nav abs">
    <div class="logo abs">vorl.</div>
    <a class="nav-home abs">Home</a>
    <a class="nav-item abs" style="left:430px">About Us</a>
    <a class="nav-item abs" style="left:530px">Sectors</a>
    <a class="nav-item abs" style="left:616px">Job Offers</a>
    <a class="nav-item abs" style="left:723px">Contact Us</a>
    <span class="nav-sep abs"></span>
    <a class="nav-item abs" style="left:850px">EN <svg width="9" height="6" viewBox="0 0 9 6"><path d="M0 0h9L4.5 6z" fill="#fff"/></svg></a>
    <a class="btn join abs">Join Now <svg class="arrow" viewBox="0 0 24 10"><path d="M0 5h22M17 1l5 4-5 4" stroke="#fff" stroke-width="1.6" fill="none"/></svg></a>
  </header>
  <h1 class="abs">Expertise serving every recruitment need</h1>
  <a class="cta cta-hire abs">I’m looking to hire <svg class="arrow" viewBox="0 0 24 10"><path d="M0 5h22M17 1l5 4-5 4" stroke="#fff" stroke-width="1.6" fill="none"/></svg></a>
  <a class="cta cta-join abs">I want to join vorl <svg class="arrow" viewBox="0 0 24 10"><path d="M0 5h22M17 1l5 4-5 4" stroke="#111" stroke-width="1.6" fill="none"/></svg></a>
  <a class="play abs"><svg width="22" height="22" viewBox="0 0 22 22"><circle cx="11" cy="11" r="11" fill="#fff"/><path d="M8 6l8 5-8 5z" fill="#000"/></svg>Play the Video</a>

  <div class="welcome abs">
    <h2 class="abs"><span>Welcome to Vorl</span></h2>
    <span class="rule abs"></span>
    <p class="abs">vorl. is a premium recruitment firm driven by experienced consultants — whether in-house or freelance — supported by a dedicated team of recruitment coordinators. Our hybrid model allows us to handle complex, confidential, or high-volume recruitment assignments with both precision and agility.</p>
    <a class="btn read-more abs">Read More <svg class="arrow" viewBox="0 0 24 10"><path d="M0 5h22M17 1l5 4-5 4" stroke="#fff" stroke-width="1.6" fill="none"/></svg></a>
  </div>

  <div class="strip abs" style="left:27px;background:linear-gradient(160deg,#6d7a6a,#3a3d3a)" role="img" aria-label="Photo of a team meeting around a conference table"></div>
  <div class="strip abs" style="left:320px;background:linear-gradient(160deg,#8a8e93,#4d5a5e)" role="img" aria-label="Photo of a job interview in progress"></div>
  <div class="strip abs" style="left:612px;background:linear-gradient(160deg,#5a6a86,#2d3442)" role="img" aria-label="Photo of two women shaking hands across a desk"></div>
  <div class="strip abs" style="left:901px;background:linear-gradient(160deg,#9aa0a3,#5b5f62)" role="img" aria-label="Photo of colleagues discussing at a meeting table"></div>
</section>

<section class="sectors abs">
  <h2 class="section-title abs">Our Sectors</h2>
  <span class="rule abs"></span>
</section>

<!-- sector cards row 1 -->
<article class="card abs" style="left:148px;top:1673px;width:215px;height:388px;background:var(--executive)">
  <div class="brand abs">vorl.<small>executive</small></div>
  <div class="icon abs" style="left:65px"><svg width="40" height="40" viewBox="0 0 40 40" fill="none" stroke="#fff" stroke-width="1.6"><circle cx="20" cy="13" r="7"/><path d="M6 36c1-9 7-13 14-13s13 4 14 13z"/></svg></div>
  <h3 class="abs">Executive</h3>
  <p class="abs">Lorem ipsum dolor sit amet, consectetur adipiscing elit, sed do eiusmod tempor incididunt ut labore et dolore magna aliqua. Ut enim ad minim veniam, quis nostrud</p>
  <a class="more abs">Read More</a>
</article>
<article class="card abs" style="left:379px;top:1673px;width:215px;height:388px;background:var(--finance)">
  <div class="brand abs">vorl.<small>finance &amp; advisory</small></div>
  <div class="icon abs" style="left:65px"><svg width="40" height="40" viewBox="0 0 40 40" fill="none" stroke="#fff" stroke-width="1.6"><rect x="5" y="12" width="30" height="20" rx="2"/><circle cx="20" cy="22" r="6"/><path d="M10 12l6-6h8l6 6"/></svg></div>
  <h3 class="abs">Finance &amp; Advisory</h3>
  <p class="abs">Lorem ipsum dolor sit amet, consectetur adipiscing elit, sed do eiusmod tempor incididunt ut labore et dolore magna aliqua. Ut enim ad minim veniam, quis nostrud</p>
  <a class="more abs">Read More</a>
</article>
<article class="card abs" style="left:606px;top:1673px;width:215px;height:388px;background:var(--legal)">
  <div class="brand abs">vorl.<small>legal</small></div>
  <div class="icon abs" style="left:65px"><svg width="40" height="40" viewBox="0 0 40 40" fill="none" stroke="#fff" stroke-width="1.6"><path d="M8 4h18l6 6v26H8z"/><path d="M13 14h14M13 19h14M13 24h8"/><circle cx="28" cy="30" r="5"/><path d="M26 30l2 2 3-3"/></svg></div>
  <h3 class="abs">Legal</h3>
  <p class="abs">Lorem ipsum dolor sit amet, consectetur adipiscing elit, sed do eiusmod tempor incididunt ut labore et dolore magna aliqua. Ut enim ad minim veniam, quis nostrud</p>
  <a class="more abs">Read More</a>
</article>
<article class="card abs" style="left:834px;top:1673px;width:217px;height:388px;background:var(--audit)">
  <div class="brand abs">vorl.<small>audit &amp; expertise</small></div>
  <div class="icon abs" style="left:66px"><svg width="40" height="40" viewBox="0 0 40 40" fill="none" stroke="#fff" stroke-width="1.6"><rect x="8" y="6" width="24" height="30" rx="2"/><rect x="15" y="3" width="10" height="6" rx="1"/><path d="M13 17l3 3 6-6M13 27h14"/></svg></div>
  <h3 class="abs">Audit &amp; Expertise</h3>
  <p class="abs">Lorem ipsum dolor sit amet, consectetur adipiscing elit, sed do eiusmod tempor incididunt ut labore et dolore magna aliqua. Ut enim ad minim veniam, quis nostrud</p>
  <a class="more abs">Read More</a>
</article>

<!-- sector cards row 2 -->
<article class="card abs" style="left:149px;top:2089px;width:290px;height:388px;background:var(--people)">
  <div class="brand abs" style="left:16px;top:14px">vorl.<small>people &amp; office</small></div>
  <div class="icon abs" style="left:103px"><svg width="40" height="40" viewBox="0 0 40 40" fill="none" stroke="#fff" stroke-width="1.6"><circle cx="20" cy="10" r="4"/><circle cx="10" cy="14" r="3.5"/><circle cx="30" cy="14" r="3.5"/><path d="M6 36c0-8 6-14 14-14s14 6 14 14"/></svg></div>
  <h3 class="abs">People &amp; Office</h3>
  <p class="abs" style="width:250px">Lorem ipsum dolor sit amet, consectetur adipiscing elit, sed do eiusmod tempor incididunt ut labore et dolore magna aliqua. Ut enim ad minim veniam, quis nostrud exercit ullamco laboris nisi ut aliquip ex ea commodo consequat. Duis aute irure dolor.</p>
  <a class="more abs">Read More</a>
</article>
<article class="card abs" style="left:455px;top:2089px;width:290px;height:388px;background:var(--supply)">
  <div class="brand abs" style="left:22px;top:14px">vorl.<small>supply &amp; purchasing</small></div>
  <div class="icon abs" style="left:103px"><svg width="40" height="40" viewBox="0 0 40 40" fill="none" stroke="#fff" stroke-width="1.6"><circle cx="20" cy="20" r="14"/><circle cx="20" cy="20" r="8"/><circle cx="20" cy="20" r="3"/></svg></div>
  <h3 class="abs">Supply &amp; Purchasing</h3>
  <p class="abs" style="width:250px">Lorem ipsum dolor sit amet, consectetur adipiscing elit, sed do eiusmod tempor incididunt ut labore et dolore magna aliqua. Ut enim ad minim veniam, quis nostrud exercit ullamco laboris nisi ut aliquip ex ea commodo consequat. Duis aute irure dolor.</p>
  <a class="more abs">Read More</a>
</article>
<article class="card abs" style="left:761px;top:2089px;width:290px;height:388px;background:var(--industry)">
  <div class="brand abs" style="left:16px;top:14px">vorl.<small>industry &amp; engineering</small></div>
  <div class="icon abs" style="left:103px"><svg width="40" height="40" viewBox="0 0 40 40" fill="none" stroke="#fff" stroke-width="1.6"><path d="M7 24a13 13 0 0 1 26 0z"/><path d="M5 24h30v4H5zM20 11v6"/><path d="M13 30c0 4 3 6 7 6s7-2 7-6"/></svg></div>
  <h3 class="abs">Industry &amp; Engineering</h3>
  <p class="abs" style="width:250px">Lorem ipsum dolor sit amet, consectetur adipiscing elit, sed do eiusmod tempor incididunt ut labore et dolore magna aliqua. Ut enim ad minim veniam, quis nostrud exercit ullamco laboris nisi ut aliquip ex ea commodo consequat. Duis aute irure dolor.</p>
  <a class="more abs">Read More</a>
</article>

<section class="values abs">
  <h2 class="section-title abs">Our Values</h2>
  <span class="rule abs"></span>

  <div class="value">
    <div class="value-icon abs" style="top:153px"><svg width="40" height="40" viewBox="0 0 40 40" fill="none" stroke="#fff" stroke-width="1.8"><path d="M20 3l14 7v10c0 9-6 14-14 17C12 34 6 29 6 20V10z"/><path d="M20 12l2.5 5 5.5.8-4 3.9 1 5.5-5-2.6-5 2.6 1-5.5-4-3.9 5.5-.8z"/></svg></div>
    <h3 class="abs" style="top:146px">Excellence</h3>
    <p class="abs" style="top:182px">Lorem ipsum dolor sit amet, consectetur adipiscing elit, sed do eiusmod tempor incididunt ut labore et dolore magna aliqua. Ut enim ad minim veniam, quis nostrud exercit ullamco laboris nisi ut aliquip.</p>
  </div>
  <span class="value-rule abs" style="top:267px"></span>
  <div class="value">
    <div class="value-icon abs" style="top:293px"><svg width="40" height="40" viewBox="0 0 40 40" fill="none" stroke="#fff" stroke-width="1.8"><path d="M6 16h8a4 4 0 1 1 8 0h8v8a4 4 0 1 0 0 8v4H6V26a4 4 0 1 0 0-8z"/><path d="M24 4l6 6M30 4v6h-6"/></svg></div>
    <h3 class="abs" style="top:286px">Flexibility</h3>
    <p class="abs" style="top:322px">Lorem ipsum dolor sit amet, consectetur adipiscing elit, sed do eiusmod tempor incididunt ut labore et dolore magna aliqua. Ut enim ad minim veniam, quis nostrud exercit ullamco laboris nisi ut aliquip.</p>
  </div>
  <span class="value-rule abs" style="top:417px"></span>
  <div class="value">
    <div class="value-icon abs" style="top:443px"><svg width="40" height="40" viewBox="0 0 40 40" fill="none" stroke="#fff" stroke-width="1.8"><path d="M4 22l8-8 6 2 6-4 6 3 6-3M10 24l8 8 4-3 4 3 6-6"/><path d="M18 18l6 6M22 16l6 6"/></svg></div>
    <h3 class="abs" style="top:436px">Partnership</h3>
    <p class="abs" style="top:472px">Lorem ipsum dolor sit amet, consectetur adipiscing elit, sed do eiusmod tempor incididunt ut labore et dolore magna aliqua. Ut enim ad minim veniam, quis nostrud exercit ullamco laboris nisi ut aliquip.</p>
  </div>

  <div class="circle-photo abs" style="left:821px;top:65px;width:194px;height:194px;background:radial-gradient(circle,#7a7f86,#2f3338)" role="img" aria-label="Photo of a business handshake"></div>
  <div class="circle-photo abs" style="left:656px;top:222px;width:218px;height:218px;background:radial-gradient(circle,#c9c6c0,#5f5c58)" role="img" aria-label="Photo of hands reviewing documents at a desk"></div>
  <div class="circle-photo abs" style="left:816px;top:282px;width:244px;height:244px;background:radial-gradient(circle,#c99a7a,#5a4034)" role="img" aria-label="Photo of colleagues working together on a laptop"></div>
</section>

<section class="approach abs">
  <div class="approach-photo abs" style="left:149px;background:linear-gradient(150deg,#8a6a4a,#3d3b3a)" role="img" aria-label="Photo of a team working around a table with charts"></div>
  <div class="approach-photo abs" style="left:619px;background:linear-gradient(150deg,#4f80b4,#1c3a5e)" role="img" aria-label="Photo of hands typing on a laptop with a network overlay"></div>

  <span class="approach-rule abs" style="left:149px;top:446px;width:420px"></span>
  <h3 class="abs" style="left:169px;top:462px">Our<br>Commitment<br>to Quality</h3>
  <ul class="points abs" style="left:378px;top:452px;width:190px">
    <li>Our Rigorous<br>Recruitment Methodology</li>
    <li>Built on transparency</li>
    <li>Client satisfaction</li>
    <li>Personalized</li>
    <li style="border-bottom:0">Tailor-made Support</li>
  </ul>

  <span class="approach-rule abs" style="left:619px;top:446px;width:416px"></span>
  <h3 class="abs" style="left:641px;top:462px">Our<br>Augmented<br>Approach</h3>
  <ul class="points abs" style="left:845px;top:452px;width:190px">
    <li>Predictive testing for<br>smarter recruitment</li>
    <li>AI-powered tools,</li>
    <li>Smart CRM systems,</li>
    <li style="border-bottom:0">Automated multi-channel<br>sourcing</li>
  </ul>
</section>

<section class="hybrid">
  <div class="hybrid-photo abs" style="background:linear-gradient(150deg,#5f6b6e,#2b2f33)" role="img" aria-label="Photo of three women in a meeting with coffee cups"></div>
  <h2 class="abs">Our Hybrid<br>Model</h2>
  <span class="rule abs"></span>
  <p class="abs">A clear and compelling look at our unique blend of employees and freelancers, combining flexibility with efficiency to deliver optimal value for our clients.</p>
</section>

<footer class="footer abs">
  <div class="logo abs">vorl.</div>
  <h4 class="abs" style="left:462px;top:60px">Menu</h4>
  <ul class="menu abs">
    <li>Home</li><li>About Us</li><li>Sectors</li><li>Job Offers</li><li>Contact Us</li>
  </ul>
  <h4 class="abs" style="left:601px;top:60px">Contact us</h4>
  <div class="field abs" style="top:89px">Full Name</div>
  <div class="field abs" style="top:131px">Email id</div>
  <div class="field abs" style="top:175px">Phone</div>
  <div class="message abs">Message</div>
  <div class="follow abs">Follow</div>
  <span class="social abs" style="left:218px;background:#2c4f9a" role="img" aria-label="Social network link"></span>
  <span class="social abs" style="left:257px;background:#111" role="img" aria-label="Social network link"></span>
  <span class="social abs" style="left:296px;background:#b8338a" role="img" aria-label="Social network link"></span>
  <span class="social abs" style="left:335px;background:#111" role="img" aria-label="Social network link"></span>
  <span class="social abs" style="left:374px;background:#2a64a8" role="img" aria-label="Social network link"></span>
  <span class="foot-line abs"></span>
  <a class="btn submit abs">Submit</a>
  <p class="copyright abs">Copyright © 2025 All Rights Reserved</p>
</footer>

</body>
</html>
```